New iOS App design for Boston Startup

We are looking for a new app design for our Zorvak app. The current app's design feels outdated and we like to add lots of new functionality and a new navigation as well. A complete overhaul therefore!
We want you to design 5 screens that will have changed the most. The complete wireframes of these 5 pages are attached in the requirements document.
Once the winning design is selected we will award the winner with the designing all other screens (40-50 screens based on the same design). This will be a separate project worth $1000. The winning designer can get more follow up work if both sides are happy about the cooperation.
We will give feedback as soon as the first screen has been uploaded for review. Final decision will be made only after all 5 screens are finished.
We hope you give it your best!
Note: will only communicate through PixelGuild (no skype),
Updates
Project Deadline Extended
Reason: Want to give designers a chance to submit their designs as I understand from some, the deadline is too close.
I have raised the award and introduced a 2nd price as well to make it worth your time. I hope you give it your best shot.
Project Deadline Extended
Reason: A few of you have asked for an extension of the deadline as time is running out. I will extend by one day. Tell me if you need more.
Industry/Entity Type
Startup
Requirements
Must have
- At least 1 screen before we can give you feedback.
Nice to have
- multiple options of 1 screen to get to a desirable design

```html
<!DOCTYPE html>
<html lang="en">
<head>
<meta charset="utf-8">
<title>Zorvak — Menu</title>
<link href="https://fonts.googleapis.com/css2?family=Inter:wght@400;500;600&display=swap" rel="stylesheet">
<style>
  :root {
    --brand-blue: #2089d6;
    --brand-blue-dark: #1b78bd;
    --canvas-bg: #f4f5f7;
    --screen-bg: #ffffff;
    --text-main: #2b2b2b;
    --text-muted: #6f6f6f;
    --divider: #e6e6e6;
    --chevron: #b9b9b9;
    --icon: #3a3a3a;
    --tab-bg: #f8f8f8;
  }
  * { box-sizing: border-box; margin: 0; padding: 0; }
  html, body {
    width: 1200px; height: 1041px; overflow: hidden;
    background: var(--canvas-bg);
    font-family: "Inter", Helvetica, Arial, sans-serif;
  }
  .app-screen {
    position: absolute; left: 330px; top: 40px;
    width: 540px; height: 960px;
    background: var(--screen-bg);
    display: flex; flex-direction: column;
    box-shadow: 0 10px 40px rgba(0,0,0,0.08);
    overflow: hidden;
  }
  .app-header { background: var(--brand-blue); color: #fff; }
  .status-bar {
    height: 29px; padding: 0 12px;
    display: flex; align-items: center; justify-content: space-between;
    font-size: 14px; font-weight: 500;
  }
  .status-left, .status-right { display: flex; align-items: center; gap: 6px; width: 160px; }
  .status-right { justify-content: flex-end; }
  .signal-dots { display: flex; gap: 3px; }
  .signal-dots span { width: 6px; height: 6px; border-radius: 50%; background: #fff; }
  .carrier { letter-spacing: 0.5px; font-size: 12px; }
  .battery { width: 30px; height: 13px; border: 1.5px solid #fff; border-radius: 3px; padding: 1px; }
  .battery span { display: block; height: 100%; background: #fff; border-radius: 1px; }
  .nav-bar {
    height: 63px; position: relative;
    display: flex; align-items: center; justify-content: center;
  }
  .nav-title { font-size: 24px; font-weight: 500; }
  .menu-toggle { position: absolute; left: 20px; top: 20px; }
  .menu-list { list-style: none; }
  .menu-item {
    height: 63px; display: flex; align-items: center;
    padding: 0 22px 0 24px;
    border-bottom: 1px solid var(--divider);
    color: var(--text-main); font-size: 20px;
  }
  .menu-icon { width: 30px; height: 30px; margin-right: 18px; flex: none; }
  .menu-label { flex: 1; }
  .menu-chevron { width: 14px; height: 14px; }
  .tab-bar {
    margin-top: auto; height: 71px; background: var(--tab-bg);
    border-top: 1px solid var(--divider);
    display: flex; justify-content: space-around; align-items: center;
  }
  .tab { display: flex; flex-direction: column; align-items: center; gap: 4px; font-size: 12px; color: var(--text-muted); width: 80px; }
  .tab svg { width: 32px; height: 28px; }
  .tab.is-active { color: var(--brand-blue); }
</style>
</head>
<body>
<main class="app-screen">
  <header class="app-header">
    <div class="status-bar">
      <div class="status-left">
        <div class="signal-dots"><span></span><span></span><span></span></div>
        <span class="carrier">KESTREL</span>
        <svg width="14" height="11" viewBox="0 0 14 11" fill="none" stroke="#fff" stroke-width="1.6"><path d="M1 4a9 9 0 0 1 12 0M3.5 6.5a5 5 0 0 1 7 0"/><circle cx="7" cy="9" r="1" fill="#fff"/></svg>
      </div>
      <span class="clock">4:21 PM</span>
      <div class="status-right">
        <svg width="9" height="13" viewBox="0 0 9 13" fill="none" stroke="#fff" stroke-width="1.3"><path d="M1 3.5l7 6-3.5 3V.5L8 3.5l-7 6"/></svg>
        <span>100%</span>
        <div class="battery"><span></span></div>
      </div>
    </div>
    <div class="nav-bar">
      <svg class="menu-toggle" width="30" height="22" viewBox="0 0 30 22" stroke="#fff" stroke-width="2.6" stroke-linecap="round"><path d="M2 3h26M2 11h26M2 19h26"/></svg>
      <h1 class="nav-title">Menu</h1>
    </div>
  </header>

  <ul class="menu-list">
    <li class="menu-item">
      <svg class="menu-icon" viewBox="0 0 30 30" fill="none" stroke="var(--icon)" stroke-width="1.6"><path d="M3 10l12-5 12 5-12 5z"/><path d="M8 12v6c0 2 3.5 4 7 4s7-2 7-4v-6"/><path d="M25 11v7"/></svg>
      <span class="menu-label">Profile</span>
      <svg class="menu-chevron" viewBox="0 0 14 14" fill="none" stroke="var(--chevron)" stroke-width="1.8"><path d="M4 2l6 5-6 5"/></svg>
    </li>
    <li class="menu-item">
      <svg class="menu-icon" viewBox="0 0 30 30" fill="none" stroke="var(--icon)" stroke-width="1.6"><circle cx="15" cy="10" r="5"/><path d="M5 26c0-6 4.5-9 10-9s10 3 10 9z"/></svg>
      <span class="menu-label">My Tutor</span>
      <svg class="menu-chevron" viewBox="0 0 14 14" fill="none" stroke="var(--chevron)" stroke-width="1.8"><path d="M4 2l6 5-6 5"/></svg>
    </li>
    <li class="menu-item">
      <svg class="menu-icon" viewBox="0 0 30 30" fill="none" stroke="var(--icon)" stroke-width="1.6"><path d="M3 19l20-8 3 2-20 8z"/><path d="M3 19l-1 3 4-1"/></svg>
      <span class="menu-label">Advanced Writing Assignment(AWA)</span>
      <svg class="menu-chevron" viewBox="0 0 14 14" fill="none" stroke="var(--chevron)" stroke-width="1.8"><path d="M4 2l6 5-6 5"/></svg>
    </li>
    <li class="menu-item">
      <svg class="menu-icon" viewBox="0 0 30 30" fill="none" stroke="var(--icon)" stroke-width="1.6"><path d="M4 14h5v12H4zM9 15l5-9c2 0 3 1 2.5 4L16 13h8c1.5 0 2.5 1.5 2 3l-2 8c-.4 1.3-1.3 2-2.5 2H9"/></svg>
      <span class="menu-label">Social</span>
      <svg class="menu-chevron" viewBox="0 0 14 14" fill="none" stroke="var(--chevron)" stroke-width="1.8"><path d="M4 2l6 5-6 5"/></svg>
    </li>
    <li class="menu-item">
      <svg class="menu-icon" viewBox="0 0 30 30" fill="none" stroke="var(--icon)" stroke-width="1.6"><path d="M15 3a11 11 0 1 1-6 20l-5 2 2-5A11 11 0 0 1 15 3z"/><path d="M12 11a3 3 0 1 1 4 3c-1 .5-1 1-1 2.5"/><circle cx="15" cy="20" r=".8" fill="var(--icon)"/></svg>
      <span class="menu-label">Vocabulary</span>
      <svg class="menu-chevron" viewBox="0 0 14 14" fill="none" stroke="var(--chevron)" stroke-width="1.8"><path d="M4 2l6 5-6 5"/></svg>
    </li>
    <li class="menu-item">
      <svg class="menu-icon" viewBox="0 0 30 30" fill="none" stroke="var(--icon)" stroke-width="1.6"><circle cx="15" cy="15" r="11"/><ellipse cx="15" cy="15" rx="5" ry="11"/><path d="M4 15h22M6 9h18M6 21h18"/></svg>
      <span class="menu-label">Marketplace</span>
      <svg class="menu-chevron" viewBox="0 0 14 14" fill="none" stroke="var(--chevron)" stroke-width="1.8"><path d="M4 2l6 5-6 5"/></svg>
    </li>
    <li class="menu-item">
      <svg class="menu-icon" viewBox="0 0 30 30" fill="none" stroke="var(--icon)" stroke-width="1.6"><circle cx="15" cy="15" r="4"/><path d="M13 3h4l.7 3.3 2.6 1.1 2.9-1.8 2.8 2.8-1.8 2.9 1.1 2.6L27 13v4l-3.3.7-1.1 2.6 1.8 2.9-2.8 2.8-2.9-1.8-2.6 1.1L17 27h-4l-.7-3.3-2.6-1.1-2.9 1.8-2.8-2.8 1.8-2.9-1.1-2.6L3 17v-4l3.3-.7 1.1-2.6-1.8-2.9 2.8-2.8 2.9 1.8 2.6-1.1z"/></svg>
      <span class="menu-label">Settings</span>
      <svg class="menu-chevron" viewBox="0 0 14 14" fill="none" stroke="var(--chevron)" stroke-width="1.8"><path d="M4 2l6 5-6 5"/></svg>
    </li>
    <li class="menu-item">
      <svg class="menu-icon" viewBox="0 0 30 30" fill="none" stroke="var(--icon)" stroke-width="1.6"><circle cx="15" cy="15" r="11"/><path d="M15 13v8"/><circle cx="15" cy="9.5" r="1" fill="var(--icon)"/></svg>
      <span class="menu-label">About the GRADEX</span>
      <svg class="menu-chevron" viewBox="0 0 14 14" fill="none" stroke="var(--chevron)" stroke-width="1.8"><path d="M4 2l6 5-6 5"/></svg>
    </li>
  </ul>

  <nav class="tab-bar">
    <div class="tab">
      <svg viewBox="0 0 32 28" fill="var(--text-muted)"><path d="M16 3L3 14h4v11h7v-7h4v7h7V14h4z"/></svg>
      <span>Home</span>
    </div>
    <div class="tab">
      <svg viewBox="0 0 32 28" fill="none" stroke="var(--text-muted)" stroke-width="1.6"><path d="M3 5h11l2 2 2-2h11v18H18l-2 2-2-2H3zM16 7v18"/></svg>
      <span>Theory</span>
    </div>
    <div class="tab is-active">
      <svg viewBox="0 0 32 28" fill="var(--brand-blue)"><path d="M4 8h8v12H4zM13 6h8v14h-8zM22 4h8v16h-8z"/></svg>
      <span>Practice</span>
    </div>
    <div class="tab">
      <svg viewBox="0 0 32 28" fill="var(--text-muted)"><path d="M8 7h16c4 0 6 5 6 11 0 4-3 5-5 2l-3-3H10l-3 3c-2 3-5 2-5-2 0-6 2-11 6-11z"/><path d="M9 10v6M6 13h6" stroke="#fff" stroke-width="1.8"/><circle cx="22" cy="11" r="1.4" fill="#fff"/><circle cx="25" cy="14" r="1.4" fill="#fff"/></svg>
      <span>Games</span>
    </div>
    <div class="tab">
      <svg viewBox="0 0 32 28" fill="var(--text-muted)"><path d="M9 24a6 6 0 0 1-1-12 8 8 0 0 1 15-2 7 7 0 0 1 1 14z"/><path d="M11 16l4 4 7-8" stroke="#fff" stroke-width="2.4" fill="none"/></svg>
      <span>Test</span>
    </div>
  </nav>
</main>
</body>
</html>
```